New Plumbing Company

We are looking for a smart and creative business card design for our new plumbing company. We are looking for creativity and originality in our business cards.

Industry/Entity Type

Plumbing

Contact Information for Business Card

Crestline Plumbing
Peter Halvane
Managing Director
Telephone Number : 0481529604
Email : service@crestlineplumbing.com.au
Website : www.crestlineplumbing.com.au
Lic. 508264K

Colors
0692cd
33a6d7
000000

Requirements
Must have
• I want the business card to be designed on a black background using the blue tones i have selected as seen in the company logo.

```html
<!DOCTYPE html>
<html lang="en">
<head>
<meta charset="utf-8">
<title>Crestline Plumbing – Business Card</title>
<link rel="stylesheet" href="https://fonts.googleapis.com/css2?family=Lato:wght@300;400&display=swap">
<style>
  :root {
    --ink: #231f20;
    --brand-blue: #0692cd;
    --band-blue: #0089d0;
    --pattern-light: #0a9ada;
    --pattern-dark: #0a7fbf;
    --paper: #ffffff;
    --text-light: #ffffff;
  }
  * { margin: 0; padding: 0; box-sizing: border-box; }
  html, body {
    width: 988px;
    height: 1200px;
    overflow: hidden;
    background: var(--paper);
    font-family: "Lato", sans-serif;
  }
  .canvas {
    position: relative;
    width: 988px;
    height: 1200px;
  }
  .card {
    position: absolute;
    left: 177px;
    width: 620px;
    height: 343px;
    border-top-left-radius: 64px;
    overflow: hidden;
  }
  /* Front */
  .card-front {
    top: 230px;
    background: var(--ink);
  }
  .brand {
    position: absolute;
    left: 52px;
    top: 72px;
    display: flex;
    align-items: center;
    gap: 26px;
  }
  .brand-dot {
    width: 104px;
    height: 104px;
    border-radius: 50%;
    background: var(--brand-blue);
    flex: none;
  }
  .brand-name {
    color: var(--text-light);
    font-weight: 300;
    line-height: 1;
  }
  .brand-name .word-main {
    display: block;
    font-size: 56px;
    letter-spacing: 0.5px;
  }
  .brand-name .word-sub {
    display: block;
    font-size: 21px;
    letter-spacing: 7px;
    margin-top: 10px;
    padding-left: 60px;
  }
  .contact {
    position: absolute;
    left: 192px;
    top: 236px;
    list-style: none;
    color: var(--text-light);
    font-size: 16.5px;
    font-weight: 400;
    line-height: 23.5px;
  }
  .name-band {
    position: absolute;
    right: 0;
    top: 0;
    width: 98px;
    height: 100%;
    background: var(--band-blue);
  }
  .name-band .person {
    position: absolute;
    left: 50%;
    top: 50%;
    transform: translate(-50%, -50%) rotate(-90deg);
    white-space: nowrap;
    color: var(--text-light);
    text-transform: uppercase;
    line-height: 1.05;
    margin-top: -30px;
  }
  .person-name {
    display: block;
    font-size: 25px;
    font-weight: 400;
    letter-spacing: 0.3px;
  }
  .person-role {
    display: block;
    font-size: 16px;
    font-weight: 400;
    letter-spacing: 0.3px;
  }
  /* Back */
  .card-back {
    top: 630px;
  }
  .back-pattern {
    position: absolute;
    inset: 0;
    background: radial-gradient(circle at 40% 50%, var(--pattern-light), var(--band-blue) 55%, var(--pattern-dark));
  }
  .back-brand {
    position: absolute;
    left: 62px;
    top: 118px;
    display: flex;
    align-items: center;
    gap: 22px;
  }
  .back-brand .brand-ring {
    width: 112px;
    height: 112px;
    border-radius: 50%;
    border: 9px solid var(--text-light);
    flex: none;
  }
  .back-brand .brand-name .word-main { font-size: 60px; }
  .licence {
    position: absolute;
    right: 41px;
    bottom: 27px;
    color: var(--text-light);
    font-size: 12px;
    font-weight: 400;
  }
</style>
</head>
<body>
<main class="canvas">
  <section class="card card-front">
    <div class="brand">
      <span class="brand-dot"></span>
      <p class="brand-name">
        <span class="word-main">Crestline</span>
        <span class="word-sub">Plumbing</span>
      </p>
    </div>
    <ul class="contact">
      <li>M. 0481 529 604</li>
      <li>E. service@crestlineplumbing.com.au</li>
      <li>www.crestlineplumbing.com.au</li>
    </ul>
    <div class="name-band">
      <p class="person">
        <span class="person-name">Peter Halvane</span>
        <span class="person-role">Managing Director</span>
      </p>
    </div>
  </section>

  <section class="card card-back">
    <div class="back-pattern" role="img" aria-label="Repeating pattern of small water drops in blue tones"></div>
    <div class="back-brand">
      <span class="brand-ring"></span>
      <p class="brand-name"><span class="word-main">Crestline</span></p>
    </div>
    <p class="licence">Lic. 508264K</p>
  </section>
</main>
</body>
</html>
```